Holbys Pet Care

Hi. I need a business card /logo for my pet care business. Im thinking about a dogs paw print. Although i do look after other pets so don't want to restrict my self. Open to suggestions on colour etc but like greens and purples.The name of my business is holby's pet care. The logo could be just an image or have holbys power care on it. An option to do either would be great. For the winner i also would like a Web page (word press template if possible) designed if you can, of course I'll pay additional for this. Look forward to your ideas!

```html
<!DOCTYPE html>
<html lang="en">
<head>
<meta charset="utf-8">
<title>Holbys Pet Care – Business Card</title>
<link rel="stylesheet" href="https://fonts.googleapis.com/css2?family=Comfortaa:wght@700&family=Questrial&family=Kaushan+Script&display=swap">
<style>
  :root {
    --page: #ffffff;
    --purple-dark: #561c6b;
    --purple-light: #6e2a84;
    --purple-ink: #5b2670;
    --cream: #efe7c9;
    --green: #8cc63f;
    --sage: #e1e4bf;
    --text: #4a4a42;
    --photo-light: #d9cdb6;
    --photo-dark: #9c8a6e;
  }
  * { margin: 0; padding: 0; box-sizing: border-box; }
  html, body {
    width: 984px;
    height: 1200px;
    overflow: hidden;
    background: var(--page);
  }
  .canvas {
    position: relative;
    width: 984px;
    height: 1200px;
  }
  .card {
    position: absolute;
    left: 46px;
    width: 901px;
    height: 495px;
  }

  /* Front */
  .card--front {
    top: 50px;
    background: linear-gradient(180deg, var(--purple-dark) 0%, var(--purple-light) 100%);
  }
  .brand {
    position: absolute;
    left: 0;
    right: 0;
    top: 0;
    bottom: 0;
    display: flex;
    align-items: center;
    justify-content: center;
    gap: 24px;
  }
  .brand__mark {
    flex: none;
    width: 64px;
    height: 64px;
    border-radius: 50%;
    background: var(--green);
  }
  .brand__name {
    font-family: "Comfortaa", sans-serif;
    font-weight: 700;
    font-size: 60px;
    line-height: 1;
    color: var(--cream);
  }

  /* Back */
  .card--back {
    top: 650px;
    background: var(--sage);
  }
  .owner {
    position: absolute;
    left: 106px;
    top: 60px;
  }
  .owner__name {
    font-family: "Comfortaa", sans-serif;
    font-weight: 700;
    font-size: 64px;
    line-height: 1;
    color: var(--purple-ink);
  }
  .owner__role {
    font-family: "Kaushan Script", cursive;
    font-size: 36px;
    line-height: 1;
    margin-top: 6px;
    margin-left: 4px;
    color: var(--purple-ink);
  }
  .contacts {
    position: absolute;
    left: 106px;
    top: 222px;
    list-style: none;
    font-family: "Questrial", sans-serif;
    font-size: 24px;
    line-height: 33px;
    color: var(--text);
  }
  .contacts__item {
    display: flex;
    align-items: flex-start;
    margin-bottom: 16px;
  }
  .contacts__icon {
    flex: none;
    width: 32px;
    height: 32px;
    margin-right: 26px;
    margin-top: 2px;
    border-radius: 50%;
    background: var(--green);
  }
  .pet-photo {
    position: absolute;
    left: 551px;
    top: 53px;
    width: 320px;
    height: 372px;
    background: linear-gradient(160deg, var(--photo-light) 0%, var(--photo-dark) 100%);
  }
</style>
</head>
<body>
<main class="canvas">
  <section class="card card--front" aria-label="Business card front">
    <div class="brand">
      <span class="brand__mark" aria-hidden="true"></span>
      <p class="brand__name">Holbys Pet Care</p>
    </div>
  </section>

  <section class="card card--back" aria-label="Business card back">
    <header class="owner">
      <h1 class="owner__name">Holby</h1>
      <p class="owner__role">pet specialist</p>
    </header>
    <ul class="contacts">
      <li class="contacts__item">
        <span class="contacts__icon" role="img" aria-label="Small cat icon"></span>
        <span>Lorem Ipsum Street,<br>12A, NJS</span>
      </li>
      <li class="contacts__item">
        <span class="contacts__icon" role="img" aria-label="Small dog icon"></span>
        <span>Information and reservation<br>123456789 / 12345667879</span>
      </li>
      <li class="contacts__item">
        <span class="contacts__icon" role="img" aria-label="Small rabbit icon"></span>
        <span>www.holbyspetcare.com</span>
      </li>
    </ul>
    <div class="pet-photo" role="img" aria-label="Photo of a puppy and a tabby kitten sitting in a woven basket"></div>
  </section>
</main>
</body>
</html>
```